Create Banner Ads for Catholic Business Directory

The orginal web page design project was cancelled and we are looking to use our remaining allocated funds for Banner Ad designs.

We need the designer to create 300x250 and matching 300x125 Banner Ads promoting ParishMarket.com. Please look at website home page with priest (will provide photo). The banner ads will be used on other religious websites to get visitors to click and visit http://ParishMarket.com and find businesses who support Catholic churches.

"Find a Business Supporting Your Church"

Can use other images than those provided. For example religious background or image of church, etc.

Would also like to see a new simple logo graphic for "Parish Trade Locator" included on this project.

Thanks. -walt
Updates

Project Deadline Extended Reason: The original web page design project was cancelled and we are wanting to use our remaining funds for nice Banner Ad designs promoting our website http://parishmarket.com Added Sunday, January 3, 2016

Target Market(s)

Catholics looking for businesses who support the church.

Industry/Entity Type

Religious

Coding

Coded - Design and coding required

Number of Pages Required

1 page

Font styles to use
Serif

Requirements
Must have
• Attractive Clean Appearance.

```html
<!DOCTYPE html>
<html lang="en">
<head>
<meta charset="utf-8">
<title>Parish Trade Locator — Banner Ads</title>
<link rel="stylesheet" href="https://fonts.googleapis.com/css2?family=Cabin:wght@400;700&display=swap">
<style>
  :root {
    --navy: #1f4e85;
    --band-blue: #0b4f96;
    --strip-blue: #3a7fc4;
    --grey-top: #55595f;
    --grey-bottom: #767d86;
    --paper: #ffffff;
    --frame: #d6d6d6;
    --photo-dark: #2f302e;
    --photo-light: #d9d9d9;
  }
  * { box-sizing: border-box; margin: 0; padding: 0; }
  html, body { width: 1200px; height: 1000px; overflow: hidden; background: var(--paper); }
  body { position: relative; font-family: "Cabin", sans-serif; }

  .brand-lockup { position: absolute; display: flex; align-items: center; color: var(--navy); font-weight: 700; text-transform: uppercase; white-space: nowrap; }
  .brand-lockup .brand-dot { border-radius: 50%; background: var(--navy); flex: none; }

  .brand-main { left: 68px; top: 62px; font-size: 27px; letter-spacing: 0.5px; }
  .brand-main .brand-dot { width: 72px; height: 72px; margin-right: 20px; }

  .banner { position: absolute; left: 349px; width: 502px; background: var(--paper); border: 1px solid var(--frame); box-shadow: 1px 2px 4px rgba(0,0,0,0.25); overflow: hidden; }
  .banner-large { top: 190px; height: 421px; }
  .banner-small { top: 656px; height: 210px; }

  .top-strip { position: absolute; left: 2px; right: 2px; top: 3px; height: 9px; background: var(--strip-blue); }
  .banner-small .top-strip { height: 8px; }

  .banner .brand-lockup { left: 17px; font-size: 16px; letter-spacing: 0.3px; }
  .banner .brand-lockup .brand-dot { width: 40px; height: 40px; margin-right: 12px; }
  .banner-large .brand-lockup { top: 32px; }
  .banner-small .brand-lockup { top: 29px; }

  .headline { position: absolute; left: 14px; color: var(--navy); font-weight: 400; letter-spacing: 1.2px; }
  .banner-large .headline { top: 96px; font-size: 27px; line-height: 50px; }
  .banner-small .headline { top: 84px; left: 17px; font-size: 21px; line-height: 34px; letter-spacing: 0.8px; }

  .priest-photo { position: absolute; background: linear-gradient(180deg, var(--photo-light) 0%, #b89c86 22%, var(--photo-dark) 40%, var(--photo-dark) 100%); border-radius: 60px 60px 4px 4px; }
  .banner-large .priest-photo { left: 246px; top: 25px; width: 245px; height: 268px; }
  .banner-small .priest-photo { left: 296px; top: 27px; width: 190px; height: 127px; }

  .action-bar { position: absolute; left: 2px; right: 2px; bottom: 2px; background: linear-gradient(180deg, var(--grey-top) 0%, var(--grey-bottom) 100%); border-top: solid var(--band-blue); }
  .banner-large .action-bar { top: 291px; border-top-width: 21px; }
  .banner-small .action-bar { top: 153px; border-top-width: 12px; }

  .action { position: absolute; display: flex; flex-direction: column; align-items: center; color: #fff; }
  .action svg { display: block; }
  .banner-large .action { top: -37px; width: 120px; font-size: 20px; letter-spacing: 0.5px; }
  .banner-large .action span { margin-top: 4px; }
  .banner-small .action { top: -25px; width: 100px; font-size: 18px; letter-spacing: 0.4px; }
  .banner-small .action span { margin-top: 1px; }

  .banner-large .action-search { left: 44px; }
  .banner-large .action-review { left: 189px; }
  .banner-large .action-connect { left: 334px; }
  .banner-small .action-search { left: 176px; }
  .banner-small .action-review { left: 276px; }
  .banner-small .action-connect { left: 378px; }
</style>
</head>
<body>
  <svg width="0" height="0" style="position:absolute" aria-hidden="true">
    <defs>
      <symbol id="icon-search" viewBox="0 0 64 64">
        <circle cx="32" cy="32" r="30" fill="#fff" stroke="#1f4e85" stroke-width="3"/>
        <circle cx="28" cy="28" r="11" fill="none" stroke="#1f4e85" stroke-width="6"/>
        <line x1="36" y1="36" x2="46" y2="46" stroke="#1f4e85" stroke-width="7" stroke-linecap="round"/>
      </symbol>
      <symbol id="icon-review" viewBox="0 0 64 64">
        <circle cx="32" cy="32" r="30" fill="#fff" stroke="#1f4e85" stroke-width="3"/>
        <circle cx="32" cy="32" r="22" fill="#1f4e85"/>
        <polyline points="22,33 29,40 43,25" fill="none" stroke="#fff" stroke-width="6" stroke-linecap="round" stroke-linejoin="round"/>
      </symbol>
      <symbol id="icon-connect" viewBox="0 0 64 64">
        <circle cx="32" cy="32" r="30" fill="#fff" stroke="#1f4e85" stroke-width="3"/>
        <path d="M36 22c9 0 15 5 15 11 0 4-2 7-6 9l3 6-8-4c-1 0-3 0-4 0-9 0-15-5-15-11s6-11 15-11z" fill="#1f4e85" stroke="#fff" stroke-width="2"/>
        <path d="M27 15c-10 0-16 5-16 12 0 4 2 7 6 9l-3 7 9-5c1 0 3 0 4 0 10 0 16-5 16-11s-6-12-16-12z" fill="#1f4e85" stroke="#fff" stroke-width="2"/>
      </symbol>
    </defs>
  </svg>

  <div class="brand-lockup brand-main"><span class="brand-dot"></span>Parish Trade Locator</div>

  <section class="banner banner-large" aria-label="300 by 250 banner">
    <div class="top-strip"></div>
    <div class="brand-lockup"><span class="brand-dot"></span>Parish Trade Locator</div>
    <h1 class="headline">Find a Business<br>Supporting Your<br>Church.</h1>
    <div class="priest-photo" role="img" aria-label="Photo of a smiling priest in clerical collar holding a red lectionary, with grey gears behind"></div>
    <div class="action-bar">
      <div class="action action-search"><svg width="66" height="66"><use href="#icon-search"/></svg><span>Search</span></div>
      <div class="action action-review"><svg width="66" height="66"><use href="#icon-review"/></svg><span>Review</span></div>
      <div class="action action-connect"><svg width="66" height="66"><use href="#icon-connect"/></svg><span>Connect</span></div>
    </div>
  </section>

  <section class="banner banner-small" aria-label="300 by 125 banner">
    <div class="top-strip"></div>
    <div class="brand-lockup"><span class="brand-dot"></span>Parish Trade Locator</div>
    <h2 class="headline">Find a Business Supporting<br>Your Church.</h2>
    <div class="priest-photo" role="img" aria-label="Head and shoulders photo of a smiling priest, with grey gears behind"></div>
    <div class="action-bar">
      <div class="action action-search"><svg width="46" height="46"><use href="#icon-search"/></svg><span>Search</span></div>
      <div class="action action-review"><svg width="46" height="46"><use href="#icon-review"/></svg><span>Review</span></div>
      <div class="action action-connect"><svg width="46" height="46"><use href="#icon-connect"/></svg><span>Connect</span></div>
    </div>
  </section>
</body>
</html>
```